Bo's RV Park & Lodge Rack Card

Bo’s RV Park & Lodge
Route 9
Alderholt NP
555-318-7402
www.bosquillcornerrvpark.example
bosquillcorner@mailbox.example

BO’S RV PARK
14 Full Service Spaces
• Electric, Water, Sewer
• Safe & convenient location
• 24 hour indoor restroom with shower
• Roamer Circle accepted

Please note: Bo’s RV Park is an unattended RV park. No reservations required. Please pull on in,
use our self-service check-in and then sit back and relax!

BO’S LODGE
• Groups – hunting, fishing, working, playing
• 2 restrooms, one is handicap accessible
• Sleeps 15 – 2 bedrooms plus a shared sleeping area with bunk beds

WHERE ARE WE?
We are located right next to Route 9 on the north side. Take the second (middle) Alderholt exit.
 30 miles west of Crane Lake (the town) on Rte 9
 10 miles west of Crane Lake (the water) on Rte 9
 30 miles east of Hollin
 60 miles south of the Northwind Harmony Grounds - northern border on Rte 604

Target Market(s)

RVers and travelers looking for overnight accommodations

Requirements
Must have
• Must have colorful eye catching top 1/3 of card.
• Must have map (can be cropped) that I have included in files.

```html
<!DOCTYPE html>
<html lang="en">
<head>
<meta charset="utf-8">
<title>Bo's RV Park &amp; Lodge Rack Card</title>
<link href="https://fonts.googleapis.com/css2?family=Lato:wght@300;400;700;900&display=swap" rel="stylesheet">
<style>
  :root{
    --bg:#c9c9cc;
    --paper:#ffffff;
    --cream:#fbeccb;
    --red:#cf2027;
    --orange:#f39325;
    --ink:#1d1d1d;
    --dark:#262626;
  }
  *{margin:0;padding:0;box-sizing:border-box}
  html,body{width:1200px;height:1200px;overflow:hidden}
  body{background:var(--bg);font-family:"Lato",sans-serif;color:var(--ink);position:relative}
  .card{position:absolute;top:40px;width:514px;height:1120px;background:var(--paper)}
  .card--front{left:70px}
  .card--back{left:618px}
  .card__inner{position:absolute;left:16px;top:16px;width:482px;height:1088px;overflow:hidden;background:var(--cream)}
  .backdrop{position:absolute;left:0;top:0}
  .abs{position:absolute}
  .center{left:0;width:100%;text-align:center}
  .wordmark{font-family:"Lato",sans-serif;font-weight:900;font-size:58px;line-height:1;top:42px}
  .wordmark--red{color:var(--red)}
  .wordmark--black{color:var(--ink)}
  .location{font-size:29px;top:116px}
  .photo-circle{position:absolute;border-radius:50%;border:6px solid #fff}
  .front-copy{font-size:23px;line-height:28px}
  .red{color:var(--red)}
  .phone{font-weight:900;font-size:42px;color:var(--red)}
  .contact{font-size:19px;line-height:24px}
  .chev{position:absolute;top:968px}
  .web-band{position:absolute;left:0;width:100%;top:1026px;height:48px;background:var(--red);color:#fff;font-weight:700;font-size:19px;line-height:48px;text-align:center}
  .web-band--dark{background:var(--dark)}
  .checks{position:absolute;left:18px;top:144px;width:450px}
  .check{position:relative;padding-left:43px;font-size:17px;line-height:20px}
  .check svg{position:absolute;left:0;top:2px}
  .check__head{color:var(--red);font-weight:900}
  .room-photo{position:absolute;top:306px;width:213px;height:116px;border:2px solid #fff}
  .where{position:absolute;left:26px;top:446px;font-size:17px;font-weight:900;color:var(--red)}
  .where-list{position:absolute;left:26px;top:474px;width:440px;list-style:none;font-size:17px;line-height:20px}
  .where-list li{position:relative;padding-left:14px;margin-bottom:7px}
  .where-list li::before{content:"";position:absolute;left:1px;top:8px;width:5px;height:5px;border-radius:50%;background:var(--ink)}
  .map{position:absolute;left:62px;top:666px;width:357px;height:267px;border:1px solid #fff}
  .back-phone{top:944px;color:#fff;font-weight:900;font-size:42px}
  .back-mail{top:992px;color:#fff;font-size:19px}
</style>
</head>
<body>

<section class="card card--front">
  <div class="card__inner">
    <svg class="backdrop" width="482" height="1074" viewBox="0 0 482 1074">
      <defs>
        <linearGradient id="sceneFill" x1="0" y1="0" x2="0" y2="1">
          <stop offset="0" stop-color="#dfe6ea"/>
          <stop offset="0.35" stop-color="#c8d1cf"/>
          <stop offset="0.55" stop-color="#8ca27a"/>
          <stop offset="1" stop-color="#94a37c"/>
        </linearGradient>
      </defs>
      <rect x="0" y="0" width="482" height="680" fill="url(#sceneFill)" role="img" aria-label="Photo of the RV park grounds with parked campers"/>
      <polygon points="0,640 482,422 482,446 0,676" fill="var(--orange)"/>
      <polygon points="0,676 482,446 482,1074 0,1074" fill="var(--cream)"/>
    </svg>

    <div class="abs center wordmark wordmark--red">Bo’s RV Park</div>
    <div class="abs center location">Alderholt, North Plains</div>

    <div class="photo-circle" role="img" aria-label="Photo of the lodge building with red and grey metal siding"
         style="left:50px;top:172px;width:384px;height:384px;background:linear-gradient(180deg,#e9eef1 0%,#c7ccd0 40%,#8f9aa0 55%,#c9b79a 75%,#b7a98e 100%)"></div>
    <div class="photo-circle" role="img" aria-label="Photo of a bunk bed room"
         style="left:66px;top:464px;width:152px;height:152px;background:linear-gradient(160deg,#e7dccb,#b98a5a 60%,#8a5a35)"></div>
    <div class="photo-circle" role="img" aria-label="Photo of the lodge common room"
         style="left:286px;top:464px;width:136px;height:136px;background:linear-gradient(160deg,#d9b98a,#a8743f 60%,#6e4a2c)"></div>

    <div class="abs center front-copy" style="top:648px;font-weight:300">Bo’s RV Park is an unattended RV park</div>
    <div class="abs center front-copy red" style="top:679px;font-weight:900">NO RESERVATIONS REQUIRED</div>
    <div class="abs center front-copy red" style="top:709px;font-weight:900">PLEASE PULL ON IN</div>
    <div class="abs center front-copy" style="top:740px;font-size:24px">Use our self-service check-in</div>
    <div class="abs center front-copy" style="top:770px;font-size:24px">and then</div>
    <div class="abs center red" style="top:810px;font-size:31px">SIT BACK AND RELAX!</div>
    <div class="abs center phone" style="top:862px">555-318-7402</div>

    <div class="abs center contact" style="top:934px">bosquillcorner@mailbox.example<br>Bo’s RV Park &amp; Lodge<br>Route 9, Alderholt NP</div>
    <svg class="chev" style="left:50px" width="36" height="40" viewBox="0 0 36 40"><path d="M16 0 L0 20 L16 40 H24 L8 20 L24 0Z M28 0 L12 20 L28 40 H36 L20 20 L36 0Z" fill="var(--red)"/></svg>
    <svg class="chev" style="left:400px" width="36" height="40" viewBox="0 0 36 40"><path d="M20 0 L36 20 L20 40 H12 L28 20 L12 0Z M8 0 L24 20 L8 40 H0 L16 20 L0 0Z" fill="var(--red)"/></svg>

    <div class="web-band">WWW.BOSQUILLCORNERRVPARK.EXAMPLE</div>
  </div>
</section>

<section class="card card--back">
  <div class="card__inner">
    <svg class="backdrop" width="482" height="1088" viewBox="0 0 482 1088">
      <polygon points="0,800 482,634 482,660 0,824" fill="var(--orange)"/>
      <polygon points="0,824 482,660 482,1088 0,1088" fill="var(--red)"/>
    </svg>

    <div class="abs center wordmark wordmark--black">Bo’s RV Park</div>

    <div class="checks">
      <div class="check"><svg width="34" height="34" viewBox="0 0 34 34"><circle cx="17" cy="17" r="17" fill="var(--red)"/><path d="M9 17 L15 23 L25 11" fill="none" stroke="#fff" stroke-width="4" stroke-linecap="round" stroke-linejoin="round"/></svg><div class="check__head">Groups</div><div>hunting, fishing, working, playing</div></div>
      <div class="check"><svg width="34" height="34" viewBox="0 0 34 34"><circle cx="17" cy="17" r="17" fill="var(--red)"/><path d="M9 17 L15 23 L25 11" fill="none" stroke="#fff" stroke-width="4" stroke-linecap="round" stroke-linejoin="round"/></svg><div class="check__head">2 Restrooms</div><div>one is handicap accessible</div></div>
      <div class="check"><svg width="34" height="34" viewBox="0 0 34 34"><circle cx="17" cy="17" r="17" fill="var(--red)"/><path d="M9 17 L15 23 L25 11" fill="none" stroke="#fff" stroke-width="4" stroke-linecap="round" stroke-linejoin="round"/></svg><div class="check__head">Sleeps 15</div><div>2 bedrooms plus a shared sleeping area with bunk beds</div></div>
    </div>

    <div class="room-photo" role="img" aria-label="Photo of a lodge bedroom" style="left:24px;background:linear-gradient(180deg,#cfc6b4,#8d7a62 60%,#5b4a3a)"></div>
    <div class="room-photo" role="img" aria-label="Photo of the lodge kitchen and common room" style="left:246px;background:linear-gradient(180deg,#e3c79b,#a97547 60%,#6f4d30)"></div>

    <div class="where">WHERE ARE WE?</div>
    <ul class="where-list">
      <li>We are located right next to Route 9 on the north side. Take the second (middle) Alderholt exit.</li>
      <li>30 miles west of Crane Lake (the town) on Rte 9</li>
      <li>10 miles west of Crane Lake (the water) on Rte 9</li>
      <li>30 miles east of Hollin</li>
      <li>60 miles south of the Northwind Harmony Grounds northern border on Rte 604</li>
    </ul>

    <div class="map" role="img" aria-label="Road map of the area around the park and the lake" style="background:linear-gradient(135deg,#f4f4f2 0%,#eef0ea 55%,#d9e0b8 75%,#cfe0ea 100%)"></div>

    <div class="abs center back-phone">555-318-7402</div>
    <div class="abs center back-mail">bosquillcorner@mailbox.example</div>

    <div class="web-band web-band--dark">WWW.BOSQUILLCORNERRVPARK.EXAMPLE</div>
  </div>
</section>

</body>
</html>
```